small auto electrical company needs new logo and business cards !!!

we are a small auto electrical company (Velmor Autos Ltd) that has been running for 13 years the logo we have was put together by dinosaurs so we are looking at re branding the company starting with business cards and a new logo we fit GPS tracking devices for young drivers through there insurance company also we fit hands free systems and dash cameras also safety locks to fleet vehicles we would like bright eye catching colours day glow and neon and quirky designs for the logo our original logo was baby blue which i have added a picture enclosed we would like double sided but have a space to write notes and prices preferably not white on back same colour throughout many thanks
Reason: Just a chance to finalise any designs we want VA logos or V logos - No vlm's and no dinosaurs lol
Business
Installs@velmorautos.co.uk
07922483617
www.Velmorautos.co.uk
Velmor Autos Ltd - Fleets and Insurance Services
- new logo design !!
- Satellite in logo or something attaining to gps
- maybe a car in the logo
- shouldnt have velmor as vlm it is VeLMOR Autos

```html
<!DOCTYPE html>
<html lang="en">
<head>
<meta charset="utf-8">
<title>Velmor Autos Ltd – Business Card</title>
<link rel="stylesheet" href="https://fonts.googleapis.com/css2?family=Montserrat:wght@300;400;600;700&family=Michroma&display=swap">
<style>
  :root {
    --charcoal: #333333;
    --amber: #ffb300;
    --paper: #ffffff;
    --ink-light: #f2f2f2;
  }
  * { box-sizing: border-box; margin: 0; padding: 0; }
  html, body {
    width: 979px; height: 1200px; overflow: hidden;
    background: var(--paper);
    font-family: "Montserrat", sans-serif;
  }
  .canvas { position: relative; width: 979px; height: 1200px; }

  .card {
    position: absolute; left: 72px; width: 835px; height: 478px;
    border-radius: 34px; overflow: hidden;
    box-shadow: 0 6px 22px rgba(0,0,0,0.35);
  }

  /* Front */
  .card-front { top: 72px; background: var(--charcoal); }
  .front-wordmark {
    position: absolute; left: 0; right: 0; top: 50%;
    transform: translateY(-50%);
    text-align: center;
    font-weight: 600; font-size: 66px; letter-spacing: 6px;
    color: var(--amber);
  }

  /* Back */
  .card-back {
    top: 651px; background: var(--charcoal);
    border: 1px solid var(--amber);
  }
  .back-brand-panel {
    position: absolute; left: 0; top: 0; bottom: 0; width: 419px;
    background: var(--paper);
    display: flex; flex-direction: column; align-items: center; justify-content: center;
    gap: 26px;
  }
  .brand-dot {
    width: 120px; height: 120px; border-radius: 50%;
    background: var(--charcoal);
  }
  .brand-name {
    font-weight: 600; font-size: 40px; letter-spacing: 4px;
    color: var(--charcoal); text-align: center; line-height: 1.15;
  }
  .back-info-panel {
    position: absolute; left: 419px; right: 0; top: 0; bottom: 0;
    color: var(--ink-light);
  }
  .company {
    position: absolute; top: 80px; left: 0; right: 0; text-align: center;
  }
  .company-name {
    font-weight: 600; font-size: 30px; color: var(--amber); letter-spacing: 0.5px;
    line-height: 1;
  }
  .company-tagline {
    font-family: "Michroma", sans-serif; font-size: 14px; letter-spacing: 5px;
    line-height: 23px; margin-top: 8px; color: var(--paper);
  }
  .person { position: absolute; top: 222px; left: 0; right: 0; text-align: center; }
  .person-name {
    font-weight: 600; font-size: 50px; letter-spacing: 4px; color: var(--amber); line-height: 1;
  }
  .person-role {
    font-weight: 600; font-size: 20px; letter-spacing: 2px; color: var(--paper); margin-top: 6px;
  }
  .contacts {
    position: absolute; left: 44px; top: 349px; list-style: none;
  }
  .contacts li {
    display: flex; align-items: center; height: 24px; margin-bottom: 16px;
    font-weight: 300; font-size: 18px; letter-spacing: 1px; color: var(--paper);
    white-space: nowrap;
  }
  .contacts svg { width: 24px; height: 24px; margin-right: 20px; flex: none; }
</style>
</head>
<body>
<div class="canvas">

  <section class="card card-front">
    <div class="front-wordmark">VELMOR AUTOS</div>
  </section>

  <section class="card card-back">
    <div class="back-brand-panel">
      <div class="brand-dot"></div>
      <div class="brand-name">VELMOR<br>AUTOS</div>
    </div>

    <div class="back-info-panel">
      <div class="company">
        <div class="company-name">VELMOR AUTOS LTD</div>
        <div class="company-tagline">FLEET &amp; INSURANCE<br>SERVICES</div>
      </div>

      <div class="person">
        <div class="person-name">RENSA</div>
        <div class="person-role">(MANAGER)</div>
      </div>

      <ul class="contacts">
        <li>
          <svg viewBox="0 0 24 24" aria-hidden="true"><rect x="2" y="5" width="20" height="14" rx="1.5" fill="#ffb300"/><path d="M3.5 7l8.5 5.5L20.5 7" fill="none" stroke="#333" stroke-width="1.8"/></svg>
          installs@velmorautos.co.uk
        </li>
        <li>
          <svg viewBox="0 0 24 24" aria-hidden="true"><path fill="#ffb300" d="M6.6 10.8a15 15 0 0 0 6.6 6.6l2.2-2.2a1 1 0 0 1 1-.25 11.4 11.4 0 0 0 3.6.57 1 1 0 0 1 1 1V20a1 1 0 0 1-1 1A17 17 0 0 1 3 4a1 1 0 0 1 1-1h3.5a1 1 0 0 1 1 1c0 1.25.2 2.45.57 3.57a1 1 0 0 1-.25 1z"/></svg>
          07922483617
        </li>
        <li>
          <svg viewBox="0 0 24 24" aria-hidden="true" fill="none" stroke="#ffb300" stroke-width="1.8"><circle cx="12" cy="12" r="9.5"/><ellipse cx="12" cy="12" rx="4" ry="9.5"/><path d="M2.5 12h19M4 7h16M4 17h16"/></svg>
          www.velmorautos.co.uk
        </li>
      </ul>
    </div>
  </section>

</div>
</body>
</html>
```